Kelvo Car Audio - Stationary Needed
Business Card, Letterhead, Envelope, Fax Cover, E-mail Signature
Kelvo Car Audio - Stationary Needed -
Creative Brief
Use specific fonts
Designers discretion
Professional
Marcus Feltin
President / CEO
4182 W. Linden Ave. Santa Ana, CA 92817
marc@kelvocaraudio.example
www.kelvocaraudio.example
For business card, use Black background w/ White font.
Would like map of our location, along with the following services we offer: - Car Audio Sales and Installation - Remote Start / Vehicle Security - GPS Navigation - iPod/Bluetooth Integration - Custom and Pre-Fab Enclosures - Professional Window Tint

```html
<!DOCTYPE html>
<html lang="en">
<head>
<meta charset="utf-8">
<title>Kelvo Car Audio – Business Card</title>
<link href="https://fonts.googleapis.com/css2?family=Open+Sans:wght@400;600;700&display=swap" rel="stylesheet">
<style>
  :root {
    --bg: #2a2a2a;
    --card: #0c0c0d;
    --white: #ffffff;
    --grey: #9a9ea3;
    --dim: #6d7176;
    --blue: #4a9fe3;
    --map-base: #e4e0d6;
    --map-road: #f2d36b;
  }
  * { margin: 0; padding: 0; box-sizing: border-box; }
  html, body { width: 1200px; height: 750px; overflow: hidden; }
  body {
    background: var(--bg);
    font-family: "Open Sans", Arial, sans-serif;
    position: relative;
  }
  .card {
    position: absolute;
    left: 324px;
    width: 504px;
    height: 295px;
    background: var(--card);
    box-shadow: 0 6px 18px rgba(0,0,0,.55);
    overflow: hidden;
  }
  .card--back { top: 53px; }
  .card--front { top: 413px; }

  .brand {
    font-weight: 700;
    color: var(--white);
    letter-spacing: .06em;
    text-transform: uppercase;
    white-space: nowrap;
  }
  .card--back .brand {
    position: absolute; right: 22px; top: 26px; font-size: 13px;
  }
  .brand-ghost {
    position: absolute; left: 50px; top: 14px;
    font-size: 40px; font-weight: 700; color: var(--white);
    opacity: .05; letter-spacing: .04em; text-transform: uppercase; white-space: nowrap;
  }
  .address {
    position: absolute; left: 55px; top: 103px;
    font-size: 8px; color: var(--dim); text-transform: uppercase; letter-spacing: .04em;
  }
  .address strong { color: var(--blue); font-weight: 600; }
  .map {
    position: absolute; left: 55px; top: 118px; width: 187px; height: 93px;
    background: linear-gradient(135deg, var(--map-base), #d8d3c6);
  }
  .website-back {
    position: absolute; left: 55px; top: 226px; width: 187px; text-align: center;
    font-size: 7.5px; color: var(--dim); letter-spacing: .08em; text-transform: uppercase;
  }
  .services {
    position: absolute; left: 276px; top: 103px;
    color: var(--white); font-size: 8px; text-transform: uppercase; letter-spacing: .03em;
  }
  .services h2 { font-size: 8px; font-weight: 600; margin-bottom: 7px; }
  .services ul { list-style: none; }
  .services li { color: var(--blue); line-height: 12.5px; }
  .services li::before { content: "- "; color: var(--grey); }

  .card--front .brand {
    position: absolute; left: 0; right: 0; top: 34px; text-align: center; font-size: 20px;
  }
  .name {
    position: absolute; left: 0; right: 0; top: 122px; text-align: center;
    font-size: 22px; font-weight: 600; color: var(--blue); text-transform: uppercase; letter-spacing: .02em;
  }
  .title {
    position: absolute; left: 0; right: 0; top: 155px; text-align: center;
    font-size: 10px; color: var(--grey);
  }
  .contact {
    position: absolute; left: 0; right: 0; top: 218px; text-align: center;
    font-size: 7.5px; color: var(--grey); letter-spacing: .04em; word-spacing: 2px;
  }
  .contact b { color: var(--blue); font-weight: 600; margin: 0 3px 0 12px; }
  .contact b:first-child { margin-left: 0; }
  .website-front {
    position: absolute; left: 0; right: 0; top: 235px; text-align: center;
    font-size: 7.5px; color: var(--white); font-weight: 600; letter-spacing: .06em; text-transform: uppercase;
  }
  .email {
    position: absolute; left: 0; right: 0; top: 248px; text-align: center;
    font-size: 7.5px; color: var(--dim);
  }
</style>
</head>
<body>
  <section class="card card--back">
    <div class="brand-ghost">Kelvo Car Audio</div>
    <div class="brand">Kelvo Car Audio</div>
    <p class="address">4182 W. Linden Ave., <strong>Santa Ana, CA 92817</strong></p>
    <div class="map" role="img" aria-label="Street map showing the shop location in Santa Ana"></div>
    <p class="website-back">www.kelvocaraudio.example</p>
    <div class="services">
      <h2>Our Services:</h2>
      <ul>
        <li>Car Audio Sales and Installation</li>
        <li>Remote Start / Vehicle Security</li>
        <li>GPS Navigation</li>
        <li>iPod/Bluetooth Integration</li>
        <li>Custom and Pre-Fab Enclosures</li>
        <li>Professional Window Tint</li>
      </ul>
    </div>
  </section>

  <section class="card card--front">
    <div class="brand">Kelvo Car Audio</div>
    <h1 class="name">Marcus Feltin</h1>
    <p class="title">President / CEO</p>
    <p class="contact"><b>PHONE:</b>555 210-4471 <b>CELL:</b>555 210-4472 <b>FAX:</b>555 210-4473</p>
    <p class="website-front">www.kelvocaraudio.example</p>
    <p class="email">marc@kelvocaraudio.example</p>
  </section>
</body>
</html>
```